New custom software business needs a Wordpress site

We need a Wordpress site for a new company based out of Chicago called 'Vellora Consulting'. Using a mix of on and off-shore resources we build custom software solutions, mainly focusing on small to medium sized companies. We help our customers "aspire" to do great things.
We have a basic site up here: https://brindlewave.example/. We worked on the content for it but not the branding. For now, this houses all the pages (except for a Contact Us page we'll be adding soon) for the foreseeable future.
We also have a new logo (attached) that we'd like to base the styling/colors on.
Target Market(s)
Small to medium sized companies that require tech resources
Industry/Entity Type
Software
Nice to have
- Teamwork, tech, professional but not elitist

```html
<!DOCTYPE html>
<html lang="en">
<head>
<meta charset="utf-8">
<title>Vellora Consulting</title>
<link href="https://fonts.googleapis.com/css2?family=Montserrat:wght@500;600;700&family=Poppins:wght@400;500;600&display=swap" rel="stylesheet">
<style>
:root{
  --brand:#0b4ea2;
  --brand-deep:#083f88;
  --accent:#4a86c5;
  --ink:#2b2f36;
  --muted:#5a5f66;
  --grey-panel:#c9d3df;
  --white:#ffffff;
}
*{box-sizing:border-box;margin:0;padding:0}
html,body{width:1200px;height:2732px;overflow:hidden}
body{font-family:"Poppins",sans-serif;color:var(--ink);background:var(--white);position:relative}
a{color:inherit;text-decoration:none}
.abs{position:absolute}

/* header */
.site-header{position:absolute;left:0;top:0;width:1200px;height:120px;background:var(--brand)}
.brand{position:absolute;left:111px;top:36px;display:flex;align-items:center;gap:14px;color:var(--white);font-family:"Poppins",sans-serif;font-weight:500;font-size:30px;letter-spacing:1px}
.brand-mark{width:34px;height:34px;border-radius:50%;background:var(--white)}
.main-nav{position:absolute;left:437px;top:52px;display:flex;gap:28px;color:var(--white);font-family:"Poppins",sans-serif;font-weight:600;font-size:14px}
.header-icons{position:absolute;left:1006px;top:42px;display:flex;gap:8px}
.round-icon{width:38px;height:38px;border-radius:50%;background:var(--white);display:flex;align-items:center;justify-content:center}

/* hero */
.hero{position:absolute;left:0;top:120px;width:1200px;height:600px;background:linear-gradient(110deg,#9aa9bb 0%,#3f6a9c 35%,#1d4a86 60%,#2a5a90 80%,#c48a3e 100%)}
.hero h1{position:absolute;left:111px;top:178px;font-family:"Montserrat",sans-serif;font-weight:600;font-size:35px;color:var(--white)}
.hero p{position:absolute;left:111px;top:236px;width:490px;font-size:19px;line-height:32px;color:var(--white)}
.btn{display:inline-block;background:var(--accent);color:var(--white);font-weight:500;font-size:17px;padding:0 27px;height:53px;line-height:53px}
.hero .btn{position:absolute;left:111px;top:364px}

/* section titles */
.section-title{position:absolute;left:0;width:1200px;text-align:center;font-family:"Montserrat",sans-serif;font-weight:600;font-size:35px;color:var(--ink)}
.title-rule{position:absolute;left:579px;width:42px;height:3px;background:var(--brand)}

/* services */
.service{position:absolute;top:928px;width:489px;height:315px;text-align:center}
.service.featured{background:var(--white);box-shadow:0 2px 14px rgba(0,0,0,.12)}
.service svg{margin-top:56px}
.service h3{font-family:"Poppins",sans-serif;font-weight:500;font-size:22px;margin-top:16px;color:#1f2329}
.service p{font-size:15px;line-height:26.5px;color:var(--muted);margin:12px 22px 0}
.service .btn{position:absolute;left:169px;top:289px}

/* why / who */
.why-panel{position:absolute;left:0;top:1437px;width:729px;height:446px;background:linear-gradient(135deg,#d3dbe5,#b9c6d5 60%,#cfd8e3)}
.why-panel h2{position:absolute;left:111px;top:54px;font-family:"Montserrat",sans-serif;font-weight:600;font-size:34px;color:#2e3440}
.why-panel .rule{position:absolute;left:111px;top:105px;width:42px;height:3px;background:var(--brand)}
.why-panel p{position:absolute;left:154px;top:138px;width:400px;font-size:15px;line-height:26.6px;color:var(--muted)}
.why-panel .btn{position:absolute;left:154px;top:331px}
.who-panel{position:absolute;left:600px;top:1371px;width:600px;height:446px;background:linear-gradient(120deg,var(--brand-deep),var(--brand) 55%,#1b5cb0)}
.who-panel h2{position:absolute;left:66px;top:58px;font-family:"Montserrat",sans-serif;font-weight:600;font-size:34px;color:var(--white)}
.who-panel .rule{position:absolute;left:66px;top:108px;width:42px;height:3px;background:var(--white)}
.who-panel p{position:absolute;left:66px;top:142px;width:400px;font-size:15px;line-height:26.6px;color:var(--white)}
.who-panel .btn{position:absolute;left:66px;top:334px;background:var(--white);color:var(--ink)}

/* insights */
.insight{position:absolute;top:2075px;width:232px;text-align:center}
.insight .photo{width:232px;height:154px}
.insight h4{margin-top:20px;font-weight:500;font-size:18px;line-height:25px;color:var(--accent)}

/* footer */
.site-footer{position:absolute;left:0;top:2392px;width:1200px;height:340px;background:var(--brand);color:var(--white)}
.site-footer .brand{left:114px;top:136px;font-size:26px}
.foot-col{position:absolute;top:60px}
.foot-col h5{font-family:"Poppins",sans-serif;font-weight:600;font-size:16px;margin-bottom:16px}
.contact-item{display:flex;gap:14px;margin-bottom:12px;font-size:13px;line-height:18px}
.contact-item b{font-weight:600;display:block}
.links a{display:block;font-size:13px;margin-bottom:14px}
.questions p{font-size:13px;line-height:23px;width:270px}
.questions u{font-weight:600}
.socials{display:flex;gap:8px;margin-top:14px}
.socials span{width:30px;height:30px;border-radius:50%;background:var(--white)}
.foot-rule{position:absolute;left:111px;top:278px;width:978px;height:1px;background:rgba(255,255,255,.7)}
.copyright{position:absolute;left:0;top:294px;width:1200px;text-align:center;font-size:14px}
</style>
</head>
<body>

<header class="site-header">
  <div class="brand"><span class="brand-mark"></span>VELLORA</div>
  <nav class="main-nav"><a href="#">SERVICES</a><a href="#">WHY VELLORA?</a><a href="#">VELLORA LEADERSHIP</a><a href="#">CONTACT US</a></nav>
  <div class="header-icons">
    <span class="round-icon"><svg width="16" height="16" viewBox="0 0 24 24"><path d="M6.6 10.8a15 15 0 0 0 6.6 6.6l2.2-2.2c.3-.3.7-.4 1-.2 1.1.4 2.3.6 3.6.6.6 0 1 .4 1 1V20c0 .6-.4 1-1 1A17 17 0 0 1 3 4c0-.6.4-1 1-1h3.5c.6 0 1 .4 1 1 0 1.3.2 2.5.6 3.6.1.3 0 .7-.2 1z" fill="#0b4ea2"/></svg></span>
    <span class="round-icon"><svg width="16" height="16" viewBox="0 0 24 24"><rect x="2" y="5" width="20" height="14" rx="2" fill="#0b4ea2"/><path d="M3 6l9 7 9-7" stroke="#fff" stroke-width="1.6" fill="none"/></svg></span>
  </div>
</header>

<section class="hero" role="img" aria-label="Upward view of glass skyscrapers against a cloudy sky">
  <h1>VELLORA CONSULTING</h1>
  <p>Welcome to Vellora, a software consulting company specializing in serving small to medium size businesses.</p>
  <a class="btn" href="#">Learn More</a>
</section>

<h2 class="section-title" style="top:820px">OUR SERVICES</h2>
<div class="title-rule" style="top:873px"></div>

<article class="service" style="left:111px">
  <svg width="62" height="64" viewBox="0 0 62 64" fill="none" stroke="#4a86c5" stroke-width="2"><circle cx="18" cy="26" r="10"/><circle cx="18" cy="26" r="4"/><circle cx="32" cy="36" r="12"/><path d="M41 45l14 14"/><path d="M42 10a7 7 0 0 1 7 7c0 3-2 4-3 6h-8c-1-2-3-3-3-6a7 7 0 0 1 7-7z"/><path d="M39 26h6M42 2v3M52 6l-2 2M32 6l2 2"/></svg>
  <h3>Custom Solution Delivery</h3>
  <p>Vellora offers a range of services focused on helping businesses and organizations deliver software solutions to their customers or users.</p>
</article>

<article class="service featured" style="left:600px">
  <svg width="64" height="64" viewBox="0 0 64 64" fill="none" stroke="#4a86c5" stroke-width="2"><circle cx="32" cy="10" r="6"/><path d="M22 30v-6a10 10 0 0 1 20 0v6"/><rect x="12" y="4" width="40" height="28"/><circle cx="32" cy="42" r="6"/><circle cx="12" cy="44" r="5"/><circle cx="52" cy="44" r="5"/><path d="M3 62v-6a9 9 0 0 1 18 0v6M43 62v-6a9 9 0 0 1 18 0v6M23 62v-4a9 9 0 0 1 18 0v4"/></svg>
  <h3>Staff Augmentation</h3>
  <p>Let Vellora help you supplement your existing software development teams with additional resources and expertise. We provided access to experienced</p>
  <a class="btn" href="#">Learn More</a>
</article>

<section class="why-panel" role="img" aria-label="Faint pale blue mountain landscape">
  <h2>WHY VELLORA?</h2>
  <div class="rule"></div>
  <p>At Vellora, we are proud to have a team of seasoned IT professionals who understand what it takes to deliver a quality solution. Our team members have a wealth of experience and expertise in a variety of different areas, including software development, system integration, data migration</p>
  <a class="btn" href="#">Learn More</a>
</section>

<section class="who-panel" role="img" aria-label="Blue tinted office towers">
  <h2>WHO WE ARE</h2>
  <div class="rule"></div>
  <p>Welcome to Vellora, a software consulting company specializing in serving small to medium size businesses. We understand the unique challenges and opportunities that these companies face, and we are dedicated to helping them succeed through innovative technology solutions.</p>
  <a class="btn" href="#">Learn More</a>
</section>

<h2 class="section-title" style="top:1979px">LATEST INSIGHTS</h2>
<div class="title-rule" style="top:2032px"></div>

<article class="insight" style="left:111px"><div class="photo" role="img" aria-label="Colleagues shaking hands across a meeting table" style="background:linear-gradient(135deg,#8a8b86,#c9c3b5 50%,#6f6b63)"></div><h4>Lorem Ipsum is<br>simply dummy text</h4></article>
<article class="insight" style="left:360px"><div class="photo" role="img" aria-label="Hands reviewing charts and reports on a desk" style="background:linear-gradient(135deg,#5f6770,#d9d6d0 50%,#c9884a)"></div><h4>Lorem Ipsum is<br>simply dummy text</h4></article>
<article class="insight" style="left:608px"><div class="photo" role="img" aria-label="Team meeting around a laptop in a bright office" style="background:linear-gradient(135deg,#9aa1a4,#e3e3df 50%,#5d5f60)"></div><h4>Lorem Ipsum is<br>simply dummy text</h4></article>
<article class="insight" style="left:857px"><div class="photo" role="img" aria-label="Team joining hands over a table" style="background:linear-gradient(135deg,#b7bcbf,#e8e8e6 50%,#4f5a66)"></div><h4>Lorem Ipsum is<br>simply dummy text</h4></article>

<footer class="site-footer">
  <div class="brand"><span class="brand-mark"></span>VELLORA</div>

  <div class="foot-col" style="left:367px">
    <h5>OUR OFFICE ADDRESS</h5>
    <div class="contact-item"><svg width="16" height="16" viewBox="0 0 24 24"><path d="M6.6 10.8a15 15 0 0 0 6.6 6.6l2.2-2.2c.3-.3.7-.4 1-.2 1.1.4 2.3.6 3.6.6.6 0 1 .4 1 1V20c0 .6-.4 1-1 1A17 17 0 0 1 3 4c0-.6.4-1 1-1h3.5c.6 0 1 .4 1 1 0 1.3.2 2.5.6 3.6.1.3 0 .7-.2 1z" fill="#9fc0e6"/></svg><div><b>Phone</b>123 456 7890</div></div>
    <div class="contact-item"><svg width="16" height="16" viewBox="0 0 24 24"><rect x="2" y="5" width="20" height="14" rx="2" fill="#9fc0e6"/><path d="M3 6l9 7 9-7" stroke="#0b4ea2" stroke-width="1.6" fill="none"/></svg><div><b>Email</b>hello@velloraconsulting.example</div></div>
    <div class="contact-item"><svg width="16" height="16" viewBox="0 0 24 24"><path d="M12 2a7 7 0 0 0-7 7c0 5 7 13 7 13s7-8 7-13a7 7 0 0 0-7-7z" fill="#9fc0e6"/><circle cx="12" cy="9" r="2.5" fill="#0b4ea2"/></svg><div><b>Location</b>Vellora Consulting<br>Lorem ipsum dolor sit amet,</div></div>
  </div>

  <div class="foot-col links" style="left:649px">
    <h5>COMPANY</h5>
    <a href="#">Services</a><a href="#">Why Vellora?</a><a href="#">Vellora Leadership</a><a href="#">Contact Us</a><a href="#">Privacy Policy</a>
  </div>

  <div class="foot-col questions" style="left:822px">
    <h5>STILL HAVE QUESTIONS?</h5>
    <p>Contact us using this form. A represental&shy;tive will answer your questions as soon as possible. <u>Contact Us</u></p>
    <div class="socials"><span></span><span></span><span></span></div>
  </div>

  <div class="foot-rule"></div>
  <div class="copyright">© 2022 All Rights Reserved</div>
</footer>

</body>
</html>
```